Skin Care Product Line needs custom designed labels

We need one to two label design templates that can be used across our natural skin care products such as body lotion, salt scrubs, lip balms, handmade soaps, body creams, body mists, foot creams, bath salts. The design will come in different colors. We have our own logo; however the logo should have the flower colored golden along with the word tavin.
Label sizes are :
1) 6 inches by 4 inches rectangular for body lotion,
2) 81/2 inches by 2 inches rectangular for body scrub,
3) 5 inches by 3 inches rectangular for body mist,
4) 2 inches by 3 inches for bath salts,
5) 2.125 inches by 2.125 inches for lip balm,
6) 11/2 inches by 1/12 inches label for soap.
Updates

The design should have a beige background with one color or two of the same colors for instance light lavender and a darker lavender. It should have a vintage feel to it because it's for a natural skin care line not commercial type. Also the fonts should be vintage looking. We can have one design with different colors such as light green, light yellow, light pink, light blue , light orange to go with the different scents. Added Tuesday, January 26, 2016

Target Market(s)

Young adults and aging boomers

Industry/Entity Type

Skin Care Product

Font styles to use
Decorative

Colors
cfeae6
b7a5cd
e4daeb
fbf289
fac994
9bcb3b
f9d9e8
f04a50
f68d4c

Requirements
Must have
• Please see attached image for design sample. Original Label design should have beige to tan colored background similar to the attached file. light colors such as lavender, light yellow, light orange, etc can be changed once original label is designed. We would need to be able to edit label design text and label design colors to match our different scents after we decide on the design.

```html
<!DOCTYPE html>
<html lang="en">
<head>
<meta charset="utf-8">
<title>Serenal Tavin – Jojoba Facial Moisturizer Labels</title>
<link href="https://fonts.googleapis.com/css2?family=Cinzel:wght@400;500&family=EB+Garamond:ital,wght@0,400;0,500;1,600&family=Pinyon+Script&display=swap" rel="stylesheet">
<style>
  :root {
    --bg-top: #ffffff;
    --bg-bottom: #e6e6e6;
    --label-light: #e2d9cb;
    --label-tan: #cfc2b1;
    --label-back: #d9cebd;
    --ink: #3a3531;
    --ink-soft: #5b534c;
    --ink-white: #f6f2ec;
    --ornament-dark: #8a827a;
    --ornament-light: #ece6dd;
    --rule: #6d655e;
  }
  * { box-sizing: border-box; margin: 0; padding: 0; }
  html, body { width: 1200px; height: 720px; overflow: hidden; }
  body {
    background: linear-gradient(180deg, var(--bg-top) 0%, var(--bg-bottom) 100%);
    font-family: "EB Garamond", serif;
    color: var(--ink);
  }
  .label-row {
    position: absolute;
    top: 135px;
    left: 85px;
    display: flex;
    gap: 80px;
  }
  .label {
    position: relative;
    width: 290px;
    height: 450px;
    text-align: center;
  }
  .label--classic { background: var(--label-light); }
  .label--tan { background: var(--label-tan); }
  .label--back { background: var(--label-back); }

  .frame {
    position: absolute;
    inset: 9px;
    border: 1.5px solid var(--ink);
  }
  .frame::after {
    content: "";
    position: absolute;
    inset: 4px;
    border: 0.75px solid var(--ink);
  }
  .label--tan .frame,
  .label--tan .frame::after { border-color: var(--ink-white); }

  .corner {
    position: absolute;
    width: 74px;
    height: 64px;
    background: var(--ornament-dark);
    opacity: 0.55;
  }
  .label--tan .corner { background: var(--ornament-light); opacity: 0.7; }
  .corner--tl { top: 16px; left: 16px; }
  .corner--tr { top: 16px; right: 16px; }
  .corner--bl { bottom: 16px; left: 16px; }
  .corner--br { bottom: 16px; right: 16px; }

  .brand {
    position: absolute;
    top: 98px;
    left: 0; right: 0;
    font-family: "Cinzel", serif;
    font-weight: 400;
    font-size: 21px;
    letter-spacing: 0.04em;
    color: var(--ink);
  }
  .flourish {
    position: absolute;
    left: 50%;
    width: 128px;
    height: 22px;
    margin-left: -64px;
    background: var(--ornament-dark);
    opacity: 0.5;
    border-radius: 11px;
  }
  .label--tan .flourish { background: var(--ornament-light); opacity: 0.75; }
  .flourish--above { top: 150px; }
  .flourish--below { top: 252px; }

  .product-name {
    position: absolute;
    top: 184px;
    left: 0; right: 0;
    font-family: "Cinzel", serif;
    font-size: 23px;
    font-weight: 400;
    color: var(--ink);
  }
  .product-type {
    position: absolute;
    top: 220px;
    left: 0; right: 0;
    font-size: 17px;
    letter-spacing: 0.08em;
    color: var(--ink-soft);
  }
  .label--tan .product-name,
  .label--tan .product-type { color: var(--ink-white); }

  .tagline {
    position: absolute;
    top: 352px;
    left: 0; right: 0;
    font-family: "Pinyon Script", cursive;
    font-size: 24px;
    color: var(--ink);
  }
  .net-weight {
    position: absolute;
    top: 394px;
    left: 0; right: 0;
    font-size: 14px;
    color: var(--ink);
  }

  .back-flourish {
    position: absolute;
    top: 40px;
    left: 50%;
    width: 120px;
    height: 24px;
    margin-left: -60px;
    background: var(--ornament-dark);
    opacity: 0.5;
    border-radius: 12px;
  }
  .copy {
    position: absolute;
    top: 84px;
    left: 24px;
    right: 24px;
    font-size: 10.4px;
    line-height: 1.42;
    text-align: justify;
    color: var(--ink);
  }
  .copy strong { font-style: italic; font-weight: 600; }
  .back-rule {
    position: absolute;
    left: 50%;
    width: 60px;
    margin-left: -30px;
    border-top: 0.75px solid var(--rule);
  }
  .back-rule--short { top: 306px; }
  .claim {
    position: absolute;
    top: 318px;
    left: 0; right: 0;
    font-size: 10.5px;
    font-style: italic;
    font-weight: 600;
  }
  .website {
    position: absolute;
    top: 343px;
    left: 0; right: 0;
    font-size: 10px;
    letter-spacing: 0.03em;
  }
  .cruelty-free {
    position: absolute;
    top: 366px;
    left: 50%;
    width: 60px;
    margin-left: -30px;
    font-size: 6.5px;
    line-height: 1.15;
    color: var(--ink-soft);
  }
  .cruelty-free .badge {
    display: block;
    width: 18px;
    height: 18px;
    margin: 0 auto 2px;
    border: 1px solid var(--ink-soft);
  }
  .back-rule--long {
    top: 410px;
    width: 176px;
    margin-left: -88px;
  }
</style>
</head>
<body>
  <main class="label-row">

    <section class="label label--classic" aria-label="Front label, dark ornament version">
      <div class="frame"></div>
      <div class="corner corner--tl" role="img" aria-label="Vintage scroll corner ornament"></div>
      <div class="corner corner--tr" role="img" aria-label="Vintage scroll corner ornament"></div>
      <div class="corner corner--bl" role="img" aria-label="Vintage scroll corner ornament"></div>
      <div class="corner corner--br" role="img" aria-label="Vintage scroll corner ornament"></div>
      <p class="brand">SERENAL TAVIN</p>
      <div class="flourish flourish--above" role="img" aria-label="Decorative scroll flourish"></div>
      <h1 class="product-name">JOJOBA FACIAL</h1>
      <p class="product-type">Moisturizer</p>
      <div class="flourish flourish--below" role="img" aria-label="Decorative scroll flourish"></div>
      <p class="tagline">Natural Products</p>
      <p class="net-weight">8 fl oz/226g</p>
    </section>

    <section class="label label--tan" aria-label="Front label, light ornament version">
      <div class="frame"></div>
      <div class="corner corner--tl" role="img" aria-label="Vintage scroll corner ornament"></div>
      <div class="corner corner--tr" role="img" aria-label="Vintage scroll corner ornament"></div>
      <div class="corner corner--bl" role="img" aria-label="Vintage scroll corner ornament"></div>
      <div class="corner corner--br" role="img" aria-label="Vintage scroll corner ornament"></div>
      <p class="brand">SERENAL TAVIN</p>
      <div class="flourish flourish--above" role="img" aria-label="Decorative scroll flourish"></div>
      <h2 class="product-name">JOJOBA FACIAL</h2>
      <p class="product-type">Moisturizer</p>
      <div class="flourish flourish--below" role="img" aria-label="Decorative scroll flourish"></div>
      <p class="tagline">Natural Products</p>
      <p class="net-weight">8 fl oz/226g</p>
    </section>

    <section class="label label--back" aria-label="Back label">
      <div class="back-flourish" role="img" aria-label="Decorative scroll flourish"></div>
      <p class="copy">
        This ultra-creamy non-greasy formula leaves the skin feeling soft while an aromatherapy of essential oils helps you relax after a long hard day.
        <strong>Ingredients:</strong> Purified Water, Isopropyl Palmitate, Chamomile, Geranium, Lavender, Mandarin, Sweet Marjoram and Patchouli, Propylene Glycol, Glyceryl Stearate, Isononyl Isononanoate, Glycerin, Lanolin Oil, Myristyl Myristate, Stearic Acid, Carbomer, Methylparaben, Diazolidinyl Urea, Iodopropynyl Butylcarbamate, Disodium EDTA, Allantoin, Triethanolamine, Sorbitan Stearate, Polysorbate, Dimethicone, Propylparaben, BHA Tenox, Aloe Vera Gel, Vitamin A, Vitamin D, Tocopheryl Acetate, fragrance.
      </p>
      <div class="back-rule back-rule--short"></div>
      <p class="claim">100% pure essential oils.</p>
      <p class="website">www.serenaltavin.com</p>
      <div class="cruelty-free">
        <span class="badge" role="img" aria-label="Cruelty-free badge"></span>
        Not Tested on Animals
      </div>
      <div class="back-rule back-rule--long"></div>
    </section>

  </main>
</body>
</html>
```